Pflegedienst sucht Flyerdesign
Zielgruppe
Wir sind ein ambulanter Pflegedienst und betreuen ca. 200 Patienten in ländlicher Region. Unsere Zielgruppe sind Pflegebedürftige aus altersbedingten Gründen oder nach Krankenhausaufenthalten. Wir setzen auf Qualität, Zuverlässigkeit, Exklusivität.
Aufgabenstellung
DIN lang Flyer. Wir werben ganz bewußt nicht mit Bildern von Senioren oder alten Menschen, weil das fast alle Pflegedienste tun. Daher setzen wir eher auf Motive aus unserer Urlaubsregion: Strand, Meer...
Unseren Firmen-Tarvo hätten wir gern als Fotoausschnitt ohne Hintergund mit dabei.
Und einen Kartenausschnitt mit unserem Einzugsgebiet fänden wir toll. Dies umfasst ca. 15 km um Laboe und Heikendorf folgende Orte: Stein, Wendtorf, Probsteierhagen, Schönkirchen und Mönkeberg.

```html
<!DOCTYPE html>
<html lang="de">
<head>
<meta charset="utf-8">
<title>Flyer Innenseiten – Pflegeteam Strandweide</title>
<link rel="stylesheet" href="https://fonts.googleapis.com/css2?family=Hind:wght@300;400&family=Roboto+Condensed:wght@700&display=swap">
<style>
  :root {
    --stage: #e6eaec;
    --paper: #ffffff;
    --berry: #a8286a;
    --slate: #7d979a;
    --slate-text: #6f8a8d;
    --body-grey: #8a9899;
    --label-grey: #8f9a9d;
    --fold: #d3d9da;
    --panel-tint: #e9ecec;
    --body-font: "Hind", Arial, sans-serif;
    --cond-font: "Roboto Condensed", "Arial Narrow", sans-serif;
  }
  * { box-sizing: border-box; margin: 0; padding: 0; }
  html, body { width: 1200px; height: 845px; overflow: hidden; }
  body { background: var(--stage); position: relative; font-family: var(--body-font); }

  .spread-label {
    position: absolute; top: 41px; left: 0; width: 1200px;
    text-align: center; font-size: 14px; color: var(--label-grey);
    letter-spacing: 0.5px; font-weight: 300;
  }

  .sheet {
    position: absolute; left: 68px; top: 68px; width: 1065px; height: 710px;
    background: var(--paper); overflow: hidden;
    box-shadow: 0 2px 10px rgba(60, 80, 85, 0.18);
  }
  .wave { position: absolute; left: 0; top: 0; width: 1065px; height: 710px; }
  .fold { position: absolute; top: 0; width: 1px; height: 710px; background: var(--fold); }
  .fold--one { left: 354px; }
  .fold--two { left: 709px; }

  .strengths-box {
    position: absolute; left: 710px; top: 428px; width: 332px; height: 254px;
    background: var(--panel-tint);
  }

  .birds {
    position: absolute; left: 27px; top: 27px; width: 96px; height: 70px;
    background: radial-gradient(ellipse at center, #b9c5c6 0%, rgba(185,197,198,0.35) 60%, rgba(255,255,255,0) 75%);
  }

  .brand {
    position: absolute; right: 27px; top: 32px;
    font-family: var(--body-font); font-weight: 400; font-size: 16px;
    line-height: 20px; color: var(--slate-text); white-space: nowrap; text-align: right;
  }

  .intro {
    position: absolute; left: 27px; top: 138px; width: 320px;
    color: var(--berry); font-size: 13.8px; line-height: 19.1px; font-weight: 400;
    white-space: nowrap;
  }
  .intro p + p { margin-top: 19px; }

  .call {
    position: absolute; left: 0; top: 556px; width: 354px; text-align: center;
    font-family: var(--cond-font); font-weight: 700; font-size: 14px;
    color: var(--berry); letter-spacing: 0.2px;
  }
  .call__number { letter-spacing: 1.2px; }

  .column {
    position: absolute; top: 139px; width: 320px;
    font-size: 11.6px; line-height: 14.3px; color: var(--body-grey); font-weight: 400;
  }
  .column--services { left: 382px; }
  .column--team { left: 737px; }
  .column--strengths { left: 737px; top: 446px; }

  .group + .group { margin-top: 19px; }
  .group__title { color: var(--berry); margin-bottom: 4.7px; }
  .group__note { margin-bottom: 4.7px; }
  .bullets { list-style: none; }
  .bullets li { position: relative; padding-left: 8px; margin-bottom: 4.8px; }
  .bullets li::before {
    content: ""; position: absolute; left: 0; top: 3.6px;
    border-left: 4px solid var(--body-grey);
    border-top: 3.5px solid transparent; border-bottom: 3.5px solid transparent;
  }
  .column--team .group + .group { margin-top: 24px; }
</style>
</head>
<body>
  <div class="spread-label">Innenseiten</div>

  <div class="sheet">
    <svg class="wave" viewBox="0 0 1065 710" aria-hidden="true">
      <path d="M0 556 C 160 628, 330 672, 520 682 L 1065 682 L 1065 710 L 0 710 Z" fill="var(--slate)"/>
    </svg>
    <div class="strengths-box"></div>
    <div class="fold fold--one"></div>
    <div class="fold fold--two"></div>

    <div class="birds" role="img" aria-label="Drei fliegende Möwen als Illustration in Grau"></div>

    <div class="brand">Pflegeteam Strandweide</div>

    <section class="intro">
      <p>Einen ambulanten Pflegedienst in Anspruch zu<br>nehmen, bedeutet im ersten Moment, fremden<br>Menschen zu vertrauen.</p>
      <p>Deswegen möchten wir uns bei einem Erst-<br>gespräch vorstellen und uns gegenseitig kennen<br>lernen. Dabei entwickeln wir mit Ihnen, Ihren<br>Angehörigen und unseren Pflegekräften ein auf<br>Sie abgestimmtes individuelles Versorgungskonzept<br>und beraten Sie natürlich gerne auch zur Finanzie-<br>rung.</p>
      <p>Im Mittelpunkt unserer Bemühungen stehen die<br>Zufriedenheit und die Lebensqualität unserer<br>Patienten. Deswegen begreifen wir unsere Arbeit<br>als einen ständigen Prozess, innerhalb dessen wir<br>die individuelle Situation der Pflegebedürftigen<br>ständig überprüfen, um ihnen die jeweils best-<br>mögliche und auf ihre Bedürfnisse optimal ab-<br>gestimmte Pflegequalität zukommen lassen zu<br>können.</p>
    </section>

    <p class="call">Rufen Sie uns gerne an: <span class="call__number">09876/1234</span></p>

    <section class="column column--services">
      <div class="group">
        <p class="group__title">Als Vertragspartner aller Kranken- und Pflegekassen<br>helfen wir, wo wir können:</p>
        <ul class="bullets">
          <li>bei Pflegebedürftigkeit</li>
          <li>bei Krankheit oder nach Entbindungen</li>
          <li>bei Behinderung und Einschränkungen im Alltag,<br>besonders bei Demenz</li>
          <li>nach Krankenhausaufenthalten oder ambulanten<br>Operationen</li>
          <li>bei Verhinderung der privaten Pflegepersonen</li>
          <li>in der letzten Lebensphase zu Hause</li>
          <li>bei Urlaub mit Pflegebedürftigkeit in unserer Region</li>
        </ul>
      </div>
      <div class="group">
        <p class="group__title">Und kümmern uns je nach Bedarf mehrmals täglich<br>um Sie:</p>
        <p class="group__note">Im Rahmen ärztlicher Verordnungen</p>
        <ul class="bullets">
          <li>versorgen wir Wunden und wechseln Verbände</li>
          <li>verabreichen wir Injektionen</li>
          <li>stellen wir Medikamente und überwachen die Einnahme</li>
          <li>ziehen wir Kompressionsstrümpfe an und aus</li>
          <li>messen wir Blutdruck und Blutzucker</li>
        </ul>
      </div>
      <div class="group">
        <p class="group__title">Im Rahmen der Pflegekasse</p>
        <ul class="bullets">
          <li>helfen wir bei der täglichen Körperpflege oder leiten Sie an</li>
          <li>beobachten wir umfassend Ihren Allgemeinzustand</li>
          <li>machen Bewegungsübungen, Spaziergänge oder<br>begleiten Sie zum Arzt oder Aktivitäten</li>
          <li>bereiten wir Ihnen Essen zu und kaufen ein</li>
          <li>unterstützen wir bei der hauswirtschaftliche Versorgung</li>
          <li>betreuen und entlasten wir Sie</li>
        </ul>
      </div>
    </section>

    <section class="column column--team">
      <div class="group">
        <p class="group__title">Oder wir vermitteln Ihnen Leistungen unserer langjährigen<br>Kooperationspartner</p>
        <ul class="bullets">
          <li>Pflegemittel, Essen auf Rädern, Krankentransporte,<br>Fußpflege, Hausnotruf etc.</li>
        </ul>
      </div>
      <div class="group">
        <p class="group__title">Unser motiviertes und freundliches Team besteht aus:</p>
        <ul class="bullets">
          <li>Examinierten Pflegefach- &amp; Führungskräften</li>
          <li>Palliativfachkräften</li>
          <li>Wundmanagern</li>
          <li>Hygienefachkräften</li>
          <li>Pflegeberatern</li>
          <li>Haus- &amp; Familienpfleger/innen</li>
          <li>Betreuungskräften &amp; Beschäftigungsassistenten</li>
          <li>Hauswirtschaftler/innen</li>
          <li>Kaufmännischen Verwaltungskräften</li>
        </ul>
      </div>
    </section>

    <section class="column column--strengths">
      <div class="group">
        <p class="group__title">Unsere Stärken:</p>
        <ul class="bullets">
          <li>sehr gute, MDK-geprüfte Pflegequalität</li>
          <li>Ehrlichkeit, Transparenz, Fairness</li>
          <li>individuelle Rundumversorgung und<br>partnerschaftlicher Umgang</li>
          <li>inhabergeführtes Unternehmen mit schlanken<br>Strukturen und über 20 Jahren Erfahrung</li>
          <li>angenehmes, familiäres Arbeitsklima</li>
        </ul>
      </div>
    </section>
  </div>
</body>
</html>
```